Vondrake - Waste to Fuel Power Needs A Website

Make website explaining the concept and the team behind the company
Updates

I will be providing A logo and Information about the company upon signed NDA.

Coding

Coded - Design and coding required

Number of Pages Required

5+ page

```html
<!DOCTYPE html>
<html lang="en">
<head>
<meta charset="utf-8">
<title>Vondrake - Waste to Fuel Power</title>
<link rel="stylesheet" href="https://fonts.googleapis.com/css2?family=Michroma&family=Arimo:wght@400;700&display=swap">
<style>
:root{
  --blue:#1b72bf;
  --green:#8cc63f;
  --ink:#222;
  --text:#333;
  --white:#fff;
  --head:'Michroma',sans-serif;
  --body:'Arimo',sans-serif;
}
*{margin:0;padding:0;box-sizing:border-box}
html,body{width:1200px;height:4187px;overflow:hidden;background:var(--white)}
body{position:relative;font-family:var(--body);color:var(--text)}
.abs{position:absolute}
.brand{font-family:var(--head);color:var(--blue);line-height:1;white-space:nowrap}
.brand-tag{font-family:var(--head);color:var(--green);line-height:1;white-space:nowrap}
.nav a{position:absolute;top:35px;font-family:var(--head);font-size:12.5px;color:var(--ink);text-decoration:none;white-space:nowrap}
.nav a.active{color:var(--green)}
.btn{position:absolute;display:flex;align-items:center;justify-content:center;font-family:var(--head);color:var(--white);text-decoration:none;font-size:14px;white-space:nowrap}
.btn-blue{background:var(--blue)}
.btn-green{background:var(--green)}
.photo{position:absolute}
.section-title{position:absolute;display:flex;align-items:center;gap:12px;font-family:var(--head);color:var(--blue);font-size:26px;line-height:1;white-space:nowrap}
.section-title.centered{justify-content:center}
.dot{width:28px;height:28px;border-radius:50%;background:var(--green);flex:none}
.rule{position:absolute;height:4px;background:var(--green)}
.kicker{position:absolute;font-size:17px;color:var(--green);text-transform:uppercase}
.para{position:absolute;font-size:15px;line-height:31px;color:var(--text)}
.center{text-align:center}
.card-title{position:absolute;font-family:var(--head);font-size:13.5px;color:var(--ink);display:flex;align-items:center;gap:10px;white-space:nowrap}
.card-text{position:absolute;font-size:14.5px;line-height:25px;color:var(--text);width:300px}
.feature-icon{position:absolute;width:92px;height:82px;background:var(--green);display:flex;align-items:center;justify-content:center}
.feature-label{position:absolute;font-family:var(--head);font-size:13px;line-height:27px;color:var(--ink);white-space:nowrap}
.footer-nav{position:absolute;left:113px;top:3913px;width:978px;height:67px;background:var(--green);display:flex;justify-content:center;align-items:center;gap:40px}
.footer-nav a{font-family:var(--head);font-size:14px;color:var(--white);text-decoration:none}
.social{position:absolute;top:4015px;width:42px;height:42px;border-radius:50%;background:var(--blue)}
</style>
</head>
<body>

<header>
  <div class="abs" style="left:97px;top:24px">
    <div class="brand" style="font-size:22px">VONDRAKE</div>
    <div class="brand-tag" style="font-size:8.5px;margin-top:7px">WASTE TO FUEL POWER</div>
  </div>
  <nav class="nav">
    <a class="active" style="left:318px">HOME</a>
    <a style="left:410px">TECHNOLOGY</a>
    <a style="left:578px">SUSTAINABILITY</a>
    <a style="left:770px">OUR TEAM</a>
  </nav>
  <a class="btn btn-blue" style="left:918px;top:21px;width:183px;height:50px">CONTACT US</a>
</header>

<section>
  <div class="abs" style="left:44px;top:102px;width:1116px;height:4px;background:var(--blue)"></div>
  <div class="photo" role="img" aria-label="Office with yellow, green and blue recycling bins and plants in the foreground"
       style="left:44px;top:106px;width:1116px;height:482px;background:linear-gradient(100deg,#6f8a4a 0%,#9fb58a 25%,#c9d0cc 55%,#aeb7b6 100%)"></div>
  <div class="abs" style="left:632px;top:165px;width:489px;height:360px;background:rgba(60,60,60,.85);text-align:center">
    <div class="brand" style="color:var(--white);font-size:22px;margin-top:56px">VONDRAKE</div>
    <div style="font-family:var(--head);color:var(--white);font-size:8px;margin-top:5px">WASTE TO FUEL POWER</div>
    <h1 style="font-family:var(--head);font-weight:400;color:var(--white);font-size:27px;line-height:42px;margin-top:20px">TURNING PLASTIC<br>WASTE INTO CLEAN<br>DIESEL ENERGY</h1>
  </div>
  <a class="btn btn-green" style="left:764px;top:435px;width:226px;height:49px">LEARN ABOUT US</a>
</section>

<section>
  <div class="section-title centered" style="left:0;top:690px;width:1200px"><span class="dot"></span>THE PROBLEM</div>
  <div class="rule" style="left:470px;top:734px;width:261px"></div>
  <div class="kicker center" style="left:0;top:763px;width:1200px">Plastic waste is one of the world's fastest growing environmental challenges</div>
  <p class="para center" style="left:160px;top:807px;width:880px">Every year millions of tons of plastic waste end up in landfills and oceans. At the same time, industries continue to rely on diesel fuel to power transportation, logistics, and heavy equipment. This imbalance creates an urgent need for solutions that reduce waste while producing reliable energy. Vondrake was created to address both problems simultaneously.</p>
</section>

<section>
  <div class="section-title centered" style="left:0;top:990px;width:1200px"><span class="dot"></span>HOW THE TECHNOLOGY WORKS</div>
  <div class="rule" style="left:370px;top:1033px;width:451px"></div>
  <div class="kicker center" style="left:0;top:1068px;width:1200px">Converting waste into energy</div>

  <div class="abs" style="left:114px;top:1132px;width:301px;height:14px;background:var(--green)"></div>
  <div class="photo" role="img" aria-label="Green waste container filled with collected plastic" style="left:114px;top:1146px;width:301px;height:236px;background:linear-gradient(160deg,#c9a52a 0%,#5d8b4f 50%,#3e5a3a 100%)"></div>
  <div class="photo" role="img" aria-label="Industrial processing reactor glowing orange inside a plant" style="left:451px;top:1132px;width:302px;height:236px;background:radial-gradient(circle at 55% 45%,#f0a23a 0%,#6a5a4c 30%,#2e3238 80%)"></div>
  <div class="abs" style="left:451px;top:1368px;width:302px;height:14px;background:var(--green)"></div>
  <div class="abs" style="left:789px;top:1132px;width:302px;height:14px;background:var(--green)"></div>
  <div class="photo" role="img" aria-label="Diesel generator machinery in a warehouse" style="left:789px;top:1146px;width:302px;height:236px;background:linear-gradient(120deg,#b77a33 0%,#4a4d52 50%,#7d8289 100%)"></div>

  <div class="card-title" style="left:114px;top:1412px">PLASTIC COLLECTION <svg width="28" height="14" viewBox="0 0 28 14"><path d="M1 7h25M19 1l7 6-7 6" stroke="#8cc63f" stroke-width="2" fill="none"/></svg></div>
  <p class="card-text" style="left:114px;top:1450px">Plastic waste is gathered from waste streams that would otherwise end up in landfills.</p>
  <div class="card-title" style="left:452px;top:1412px">ADVANCED PROCESSING <svg width="28" height="14" viewBox="0 0 28 14"><path d="M1 7h25M19 1l7 6-7 6" stroke="#8cc63f" stroke-width="2" fill="none"/></svg></div>
  <p class="card-text" style="left:451px;top:1450px">Plastic waste is gathered from waste streams that would otherwise end up in landfills.</p>
  <div class="card-title" style="left:789px;top:1412px">FUEL PRODUCTION <svg width="28" height="14" viewBox="0 0 28 14"><path d="M1 7h25M19 1l7 6-7 6" stroke="#8cc63f" stroke-width="2" fill="none"/></svg></div>
  <p class="card-text" style="left:789px;top:1450px">Plastic waste is gathered from waste streams that would otherwise end up in landfills.</p>
</section>

<section class="abs" style="left:0;top:1640px;width:1200px;height:618px;background:var(--blue)">
  <div class="abs" style="left:110px;top:90px;width:22px;height:422px;background:var(--green)"></div>
  <div class="photo" role="img" aria-label="Four business people reviewing a tablet together" style="left:132px;top:90px;width:406px;height:422px;background:linear-gradient(135deg,#d9dde0 0%,#b7b1a8 45%,#4d5f7c 100%)"></div>
  <div class="section-title" style="left:598px;top:110px;color:var(--white)"><span class="dot"></span>OUR TEAM</div>
  <div class="rule" style="left:678px;top:154px;width:206px"></div>
  <div class="abs" style="left:598px;top:183px;font-size:17px;color:var(--white)">THE PEOPLE BEHIND VONDRAKE</div>
  <p class="para" style="left:598px;top:233px;width:488px;color:var(--white);text-align:justify;line-height:30.5px">Vondrake is led by a team of experienced entrepreneurs, industry professionals, and strategic partners committed to developing innovative energy solutions. Our leadership brings together expertise in energy technology, business development, environmental sustainability, and industrial operations to build scalable solutions that transform plastic waste into valuable fuel.</p>
  <a class="btn btn-green" style="left:598px;top:452px;width:228px;height:50px">MEET OUR TEAM</a>
</section>

<section>
  <div class="section-title" style="left:115px;top:2402px"><span class="dot"></span>OUR SOLUTION</div>
  <div class="rule" style="left:162px;top:2443px;width:264px"></div>
  <div class="kicker" style="left:114px;top:2477px">Plastic to diesel energy</div>
  <p class="para" style="left:114px;top:2509px;width:470px;text-align:justify;line-height:30.5px">Vondrake uses advanced processing technology to convert plastic waste into usable diesel fuel. The process safely transforms non-recyclable plastics into valuable energy, reducing landfill waste and supporting industries that rely on diesel.</p>
  <div class="photo" role="img" aria-label="Green processing plant with industrial robotic arm" style="left:650px;top:2380px;width:424px;height:270px;background:linear-gradient(120deg,#5f6a70 0%,#5a9a45 45%,#c9a43a 80%,#6b7075 100%)"></div>
  <div class="abs" style="left:1074px;top:2380px;width:17px;height:270px;background:var(--green)"></div>

  <div class="feature-icon" style="left:115px;top:2728px"><svg width="40" height="48" viewBox="0 0 40 48" fill="none" stroke="#fff" stroke-width="3"><path d="M4 10h32M14 10V5h12v5M8 10l3 34h18l3-34"/></svg></div>
  <div class="feature-label" style="left:114px;top:2843px">REDUCES PLASTIC<br>WASTE</div>
  <div class="feature-icon" style="left:370px;top:2728px"><svg width="40" height="50" viewBox="0 0 40 50" fill="none" stroke="#fff" stroke-width="3"><path d="M4 8h22l10 10v28H4z"/><path d="M20 20c-5 7-7 10-7 14a7 7 0 0 0 14 0c0-4-2-7-7-14z"/></svg></div>
  <div class="feature-label" style="left:368px;top:2843px">PRODUCES USABLE<br>DIESEL FUEL</div>
  <div class="feature-icon" style="left:625px;top:2728px"><svg width="50" height="50" viewBox="0 0 50 50" fill="none" stroke="#fff" stroke-width="3"><rect x="12" y="12" width="26" height="26"/><circle cx="25" cy="25" r="6"/><path d="M25 2v8M25 40v8M2 25h8M40 25h8"/></svg></div>
  <div class="feature-label" style="left:622px;top:2843px">SUPPORTS CIRCULAR<br>ENERGY SYSTEMS</div>
  <div class="feature-icon" style="left:880px;top:2722px"><svg width="46" height="42" viewBox="0 0 46 42" fill="none" stroke="#fff" stroke-width="3"><rect x="3" y="8" width="40" height="31"/><path d="M16 8V3h14v5"/><circle cx="23" cy="24" r="6"/></svg></div>
  <div class="feature-label" style="left:877px;top:2843px">PROVIDES SCALABLE<br>INDUSTRIAL</div>
</section>

<section>
  <div class="photo" role="img" aria-label="Solar panel field and electrical substation with engineers in hard hats" style="left:0;top:3000px;width:1200px;height:703px;background:linear-gradient(180deg,#b8c4cc 0%,#8fa07a 40%,#3f5470 70%,#6c7f5a 100%)"></div>
  <div class="abs" style="left:113px;top:3063px;width:963px;height:359px;background:var(--blue)"></div>
  <div class="section-title centered" style="left:113px;top:3122px;width:963px;color:var(--white)"><span class="dot"></span>PARTNER WITH VONDRAKE</div>
  <div class="rule" style="left:406px;top:3168px;width:377px"></div>
  <p class="para center" style="left:160px;top:3197px;width:870px;color:var(--white);line-height:30.5px">Join us in transforming plastic waste into a valuable energy resource. Vondrake works with commercial diesel buyers, waste management partners, and industry leaders to deliver innovative plastic-to-diesel fuel solutions that support both energy demand and environmental responsibility.</p>
  <a class="btn btn-green" style="left:465px;top:3350px;width:270px;height:50px">CONTACT OUR TEAM</a>
</section>

<footer>
  <div class="abs" style="left:113px;top:3800px">
    <div class="brand" style="font-size:36px">VONDRAKE</div>
    <div class="brand-tag" style="font-size:16px;margin-top:10px">WASTE TO FUEL POWER</div>
  </div>
  <div class="abs" style="right:110px;top:3790px;text-align:right;font-family:var(--head);font-size:20px;line-height:36px;color:var(--ink);white-space:nowrap">TURNING PLASTIC WASTE INTO<br>SUSTAINABLE ENERGY</div>
  <nav class="footer-nav">
    <a>HOME</a><a>TECHNOLOGY</a><a>SUSTAINABILITY</a><a>OUR TEAM</a><a>CONTACT</a>
  </nav>
  <span class="social" style="left:532px" aria-label="Social profile"></span>
  <span class="social" style="left:578px" aria-label="Social profile"></span>
  <span class="social" style="left:624px" aria-label="Social profile"></span>
  <div class="abs" style="left:0;top:4130px;width:1200px;height:1px;background:#999"></div>
  <div class="abs center" style="left:0;top:4152px;width:1200px;font-family:var(--head);font-size:12px;color:var(--ink)">© 2026 VONDRAKE. ALL RIGHTS RESERVED.</div>
</footer>

</body>
</html>
```